the halvorsen group premier division

design a DL A4 tri fold brochure to reflect our creative landscape business
my web site www.thehalvorsengroup.com.au
has all the information needed
i will also be updating the website to be more updated and creative design

```html
<!DOCTYPE html>
<html lang="en">
<head>
<meta charset="utf-8">
<title>The Halvorsen Group – Brochure Cover</title>
<link href="https://fonts.googleapis.com/css2?family=Montserrat:wght@500;700&display=swap" rel="stylesheet">
<style>
  :root{
    --backdrop:#e6e6e6;
    --paper:#eeeeee;
    --ink:#262626;
    --accent:#e38b1e;
    --photo-green:#5f7d4a;
    --photo-stone:#7b7d7c;
    --leaf:#c9cdc8;
    --white:#ffffff;
  }
  *{box-sizing:border-box;margin:0;padding:0}
  html,body{width:1200px;height:907px;overflow:hidden}
  body{background:var(--backdrop);font-family:"Montserrat",sans-serif;position:relative}
  .cover{
    position:absolute;left:402px;top:33px;width:396px;height:840px;
    background:var(--paper);overflow:hidden;
    box-shadow:0 2px 10px rgba(0,0,0,.12);
  }
  .cover__photo{
    position:absolute;left:0;top:0;width:100%;height:385px;
    background:linear-gradient(170deg,#dfe3df 0%,#8fa77a 18%,var(--photo-green) 40%,#9a9c9a 62%,var(--photo-stone) 82%,#5e5f5f 100%);
  }
  .cover__leaves{position:absolute;border-radius:50%;opacity:.55}
  .cover__leaves--upper{left:-30px;top:395px;width:190px;height:170px;
    background:radial-gradient(circle,var(--leaf) 0%,rgba(201,205,200,0) 70%)}
  .cover__leaves--lower{right:-40px;top:600px;width:230px;height:240px;
    background:radial-gradient(circle,var(--leaf) 0%,rgba(201,205,200,0) 70%)}
  .brand{
    position:absolute;left:150px;top:348px;width:200px;height:100px;
    background:var(--white);
    display:flex;flex-direction:column;align-items:center;justify-content:center;gap:6px;
  }
  .brand__frame{
    position:absolute;left:162px;top:336px;width:200px;height:100px;
    border:2px solid var(--accent);
  }
  .brand__mark{width:12px;height:12px;border-radius:50%;background:var(--accent)}
  .brand__name{font-weight:700;font-size:15px;color:var(--ink);text-align:center;line-height:1.2}
  .headline{
    position:absolute;left:52px;top:505px;
    font-weight:700;font-size:27px;line-height:1.22;color:var(--ink);
  }
  .headline__rule{
    position:absolute;left:90px;top:612px;width:290px;height:3px;background:var(--accent);
  }
</style>
</head>
<body>
  <main class="cover">
    <div class="cover__photo" role="img" aria-label="Photograph of a modern outdoor patio with white chairs, stepping stones and lush garden planting"></div>
    <div class="cover__leaves cover__leaves--upper" role="img" aria-label="Faint monstera leaf illustration"></div>
    <div class="cover__leaves cover__leaves--lower" role="img" aria-label="Faint monstera leaf illustration"></div>
    <div class="brand__frame"></div>
    <div class="brand">
      <span class="brand__mark"></span>
      <span class="brand__name">The Halvorsen Group<br>Premier Division</span>
    </div>
    <h1 class="headline">Creative<br>Landscape Design<br>&amp; Construction</h1>
    <div class="headline__rule"></div>
  </main>
</body>
</html>
```